Commercial/Corporate Law Firm needs Website Design

Hi guys. I've started up a new law firm and would love your help designing an attractive website. I'll need both design and coding, and to make it easy for us to edit as necessary later, I think it should be built off a Wordpress.org structure.
FIRST IMPRESSIONS
It's very important that the first impression of the website really captures our prospective clients' attention and impresses them. Their first three seconds needs to be good.
I imagine the homepage may be short, with a menu bar and a compelling image, and with a tagline overlaid or underneath (eg. "It's about results.")
The image should be related to our practice areas: eg. IPOs, corporate transactions, or commercial negotiations.
I have previously suggested there could be a skyline image of Sydney or Adelaide. However, because we are based in Adelaide, I don't think Sydney is appropriate - and Adelaide is probably too boring to use.
HOMEPAGE
Being a new firm, we don't have many existing testimonials, and I will be the only lawyer to start with. So we need to focus on the nature of the services we will provide and how my experience can help them. We have an existing logo to use, and I would like the website colour scheme not to clash with that logo (dark blue and white).
After the initial image and tagline there should be a brief introduction to each of the main areas of work, eg. "We specialise in three main areas of practice:"
1. Corporate Transactions and Regulation
2. Business Law and Dispute Resolution
3. Migration Assistance
These should each have an appropriate photo and link to a separate page that briefly describes our services in that area.
Below that there should be a message from me with a photo. Finally, at the bottom, there should be a "Contact Us" section which shows a Google image of our address, contact details, and then our logo with colours inverted.
OTHER PAGES
While we will need some other pages, they should all be fairly simple. I think we will need one page to say "About Us", where I will put information about my experience. I think we will then need one page for each of the 3 areas listed above, which just needs an appropriate image and then text to describe the service. Finally, a "Contact Us" page which I imagine will be the same as the bottom of the homepage.
OTHER DETAILS
For now you can use details from my LinkedIn page to fill out any other text as necessary, or the photo.
Because the logo is square, I would prefer the design of the website also to be rectangular.
Looking forward to seeing your work! Thank you.
Good luck,
Marcus
Target Market(s)
Potential clients:
Businesses with legal issues or disputes
Companies wishing to list on the stock market

```html
<!DOCTYPE html>
<html lang="en">
<head>
<meta charset="utf-8">
<title>Corvane Legal</title>
<link href="https://fonts.googleapis.com/css2?family=Cinzel:wght@400;600;700&family=Lato:wght@400;700&display=swap" rel="stylesheet">
<style>
:root{
  --navy:#1b3461;
  --navy-deep:#142849;
  --ink:#0b0b0d;
  --grey-bg:#efefef;
  --text-grey:#8a8a8a;
  --white:#ffffff;
  --line:#cfcfcf;
  --brand-blue:#3f5f97;
}
*{box-sizing:border-box;margin:0;padding:0}
html,body{width:1200px;height:2885px;overflow:hidden}
body{position:relative;background:var(--white);font-family:Arial,Helvetica,sans-serif;color:#333}
.abs{position:absolute}

/* header */
.site-header{left:0;top:0;width:1200px;height:115px;background:var(--ink);border-top:4px solid var(--navy)}
.brand{left:78px;top:22px;display:flex;align-items:center;gap:12px}
.brand-mark{width:40px;height:40px;background:var(--navy)}
.brand-name{font-family:'Cinzel',serif;font-size:20px;font-weight:600;color:var(--brand-blue);letter-spacing:2px;line-height:1}
.quote-btn{left:916px;top:0;width:206px;height:52px;background:var(--navy);color:var(--white);font-family:'Cinzel',serif;font-weight:600;font-size:17px;display:flex;align-items:center;justify-content:center;border-radius:0 0 6px 6px}
.main-nav a{position:absolute;top:64px;height:51px;display:flex;align-items:center;color:var(--white);font-size:15px;text-decoration:none}
.main-nav .active{left:556px;width:104px;justify-content:center;background:var(--navy);border-radius:6px 6px 0 0}
.search-icon{left:1104px;top:80px}

/* hero */
.hero{left:0;top:115px;width:1200px;height:563px;
  background:
    linear-gradient(90deg,rgba(10,14,24,.55) 0%,rgba(10,14,24,.15) 45%,rgba(10,14,24,0) 60%),
    radial-gradient(ellipse 55% 28% at 45% 62%,rgba(235,190,120,.22),rgba(235,190,120,0) 70%),
    radial-gradient(ellipse 30% 20% at 88% 70%,rgba(235,190,120,.16),rgba(235,190,120,0) 70%),
    linear-gradient(180deg,#31456d 0%,#3a5282 22%,#2a3a5c 48%,#1c263b 72%,#10151f 100%)}
.hero-figure{left:660px;top:140px;width:500px;height:538px;
  background:
    radial-gradient(ellipse 18% 40% at 50% 68%,rgba(235,235,240,.35),rgba(235,235,240,0) 80%),
    radial-gradient(ellipse 60% 75% at 50% 100%,rgba(38,40,48,.95) 0%,rgba(38,40,48,.85) 50%,rgba(38,40,48,0) 100%)}
.hero-title{left:78px;top:288px;font-family:'Lato',sans-serif;font-weight:700;font-size:64px;line-height:76px;color:var(--white)}
.hero-text{left:78px;top:380px;width:540px;font-family:'Lato',sans-serif;font-size:17px;line-height:28px;color:var(--white)}
.btn{background:var(--navy);color:var(--white);font-family:'Cinzel',serif;font-weight:600;font-size:21px;display:flex;align-items:center;justify-content:center;border-radius:4px}
.hero-btn{left:78px;top:488px;width:196px;height:52px}
.dots{left:548px;top:634px;display:flex;gap:6px}
.dots span{width:14px;height:14px;border:2px solid #7d8aa6;border-radius:50%}
.dots .on{background:#7d8aa6}

/* practice */
.practice{left:0;top:678px;width:1200px;height:677px;background:var(--grey-bg)}
.section-title{width:1200px;left:0;text-align:center;font-family:'Cinzel',serif;font-weight:600;color:var(--navy);line-height:46px;text-transform:uppercase}
.practice-title{top:730px;font-size:40px}
.card{top:858px;width:322px;height:437px;background:var(--white);border-radius:8px;overflow:hidden}
.card.featured{background:var(--navy)}
.card-head{height:80px;background:var(--navy);color:var(--white);font-family:'Cinzel',serif;font-weight:600;font-size:17px;line-height:26px;display:flex;align-items:center;justify-content:center;text-align:center;padding:0 20px}
.card-img{height:189px}
.card-text{padding:20px 26px 0;text-align:center;font-size:13.5px;line-height:26px;color:#777}
.featured .card-text{color:#dbe2ee}
.read-more{position:absolute;left:0;width:100%;top:383px;text-align:center;font-family:'Cinzel',serif;font-weight:600;font-size:16px;color:var(--navy);text-decoration:underline}
.featured .read-more{color:var(--white)}

/* welcome */
.welcome-title{left:78px;top:1412px;font-family:'Cinzel',serif;font-weight:600;font-size:38px;color:var(--navy)}
.welcome-text{left:78px;top:1474px;width:590px;font-size:14px;line-height:26px;color:var(--text-grey)}
.welcome-text p+p{margin-top:16px}
.welcome-btn{left:78px;top:1668px;width:196px;height:52px}
.welcome-img{left:706px;top:1423px;width:416px;height:312px;background:linear-gradient(135deg,#d9dee4,#9ba6b2 60%,#4a5566)}

/* cta */
.cta{left:0;top:1800px;width:1200px;height:313px;background:linear-gradient(90deg,#223c6c,#2d4c82 50%,#223c6c)}
.cta-mark{left:573px;top:1842px;width:54px;height:54px;border:3px solid var(--white);background:var(--navy)}
.cta-title{left:0;top:1906px;width:1200px;text-align:center;font-family:'Cinzel',serif;font-weight:600;font-size:30px;line-height:44px;color:var(--white)}
.cta-btn{left:450px;top:2000px;width:300px;height:50px;border:2px solid var(--white);border-radius:4px;color:var(--white);font-family:'Cinzel',serif;font-weight:600;font-size:21px;display:flex;align-items:center;justify-content:center}

/* contact */
.contact-title{top:2166px;font-size:40px}
.contact-sub{left:0;top:2225px;width:1200px;text-align:center;font-size:16px;color:#111}
.field{border:1px solid var(--line);background:var(--white);font-size:13px;color:#666;padding:14px 12px}
.submit-btn{left:517px;top:2437px;width:165px;height:51px}

/* footer */
.foot-nav{left:0;top:2553px;width:1200px;height:72px;background:var(--navy);display:flex;justify-content:center;align-items:center;gap:48px;color:var(--white);font-size:15px}
.foot-nav span::before{content:"";display:inline-block;width:8px;height:8px;border-radius:50%;background:var(--white);margin-right:14px;vertical-align:middle}
.site-footer{left:0;top:2625px;width:1200px;height:260px;background:var(--ink)}
.foot-brand{left:84px;top:2660px;width:220px;text-align:center}
.foot-brand .brand-mark{width:72px;height:72px;margin:0 auto 14px}
.foot-brand .brand-name{font-size:28px;line-height:34px}
.copy{margin-top:12px;font-size:14px;line-height:22px;color:#8a8a8a}
.copy b{font-weight:400;color:var(--brand-blue)}
.foot-head{top:2655px;font-family:'Cinzel',serif;font-weight:600;font-size:17px;color:var(--white)}
.foot-list{left:350px;top:2697px;width:210px;list-style:none;font-size:14px;line-height:24px;color:#8a8a8a}
.foot-list li{position:relative;padding-left:20px;margin-bottom:14px}
.foot-list li::before{content:"";position:absolute;left:0;top:9px;width:6px;height:6px;background:var(--navy)}
.foot-contact{left:612px;top:2700px;width:240px;font-size:14px;line-height:24px;color:#8a8a8a}
.foot-contact div{display:flex;gap:18px;margin-bottom:26px;align-items:flex-start}
.social{left:897px;top:2702px;width:42px;height:42px;background:var(--navy);border-radius:4px}
</style>
</head>
<body>

<header class="abs site-header">
  <div class="abs brand"><span class="brand-mark"></span><span class="brand-name">CORVANE LEGAL</span></div>
  <div class="abs quote-btn">GET A FREE QUOTE</div>
  <nav class="main-nav">
    <a class="active">HOME</a>
    <a style="left:703px">ABOUT</a>
    <a style="left:795px">PRACTICE AREAS</a>
    <a style="left:972px">CONTACT US</a>
  </nav>
  <svg class="abs search-icon" width="20" height="20" viewBox="0 0 20 20"><circle cx="8" cy="8" r="6" fill="none" stroke="#3f5f97" stroke-width="3"/><line x1="12.5" y1="12.5" x2="18" y2="18" stroke="#3f5f97" stroke-width="3"/></svg>
</header>

<section>
  <div class="abs hero" role="img" aria-label="Lit city skyline at dusk above a harbour waterfront"></div>
  <div class="abs hero-figure" role="img" aria-label="Smiling lawyer in a dark suit and red tie"></div>
  <h1 class="abs hero-title">We Get Results</h1>
  <p class="abs hero-text">Lorem Ipsum is simply dummy text of the printing and type setting industry Lorem Ipsum has Lorem Ipsum is simply dummy text of the printing and type setting industry.</p>
  <div class="abs btn hero-btn">CONTACT US</div>
  <div class="abs dots"><span></span><span></span><span></span><span class="on"></span><span></span></div>
</section>

<section>
  <div class="abs practice"></div>
  <h2 class="abs section-title practice-title">We Specialise in Three Main<br>Areas of Practice</h2>

  <article class="abs card" style="left:78px">
    <div class="card-head">CORPORATE TRANSACTIONS AND REGULATION</div>
    <div class="card-img" role="img" aria-label="Business handshake" style="background:linear-gradient(135deg,#eef0f3,#9aa4b3 55%,#3d4656)"></div>
    <p class="card-text">Lorem Ipsum is simply dummy text of the printing and typesetting industry Lorem Ipsum is simply dummy text.</p>
    <span class="read-more">READ MORE</span>
  </article>

  <article class="abs card featured" style="left:438px">
    <div class="card-head">BUSINESS LAW AND DISPUTE RESOLUTION</div>
    <div class="card-img" role="img" aria-label="Signing a contract at a desk" style="background:linear-gradient(135deg,#c7ccd3,#f1f2f4 50%,#7a838f)"></div>
    <p class="card-text">Lorem Ipsum is simply dummy text of the printing and typesetting industry Lorem Ipsum is simply dummy text.</p>
    <span class="read-more">READ MORE</span>
  </article>

  <article class="abs card" style="left:800px">
    <div class="card-head">MIGRATION<br>ASSISTANCE</div>
    <div class="card-img" role="img" aria-label="Immigration law document with glasses" style="background:linear-gradient(135deg,#e8dcc8,#b48a62 55%,#5a3a24)"></div>
    <p class="card-text">Lorem Ipsum is simply dummy text of the printing and typesetting industry Lorem Ipsum is simply dummy text.</p>
    <span class="read-more">READ MORE</span>
  </article>
</section>

<section>
  <h2 class="abs welcome-title">WELCOME TO CORVANE</h2>
  <div class="abs welcome-text">
    <p>Lorem Ipsum is simply dummy text of the printing and typesetting industry. Lorem Ipsum has been the industry's standard dummy text ever since the s, when an.</p>
    <p>Lorem Ipsum is simply dummy text of the printing and typesetting industry. Lorem Ipsum has been the industry's standard dummy text ever since the 1500s, when an unknown printer took a galley of type and scrambled it to make a type specimen book. It has survived not only five centuries, but also the leap into electronic typesetting</p>
  </div>
  <div class="abs btn welcome-btn">LEARN MORE</div>
  <div class="abs welcome-img" role="img" aria-label="Smiling lawyer with arms crossed in a bright office, colleagues behind"></div>
</section>

<section>
  <div class="abs cta" role="img" aria-label="Blue-toned handshake background"></div>
  <div class="abs cta-mark"></div>
  <h2 class="abs cta-title">IF YOU NEED AN HAVE QUESTION JUST CONTACT<br>OUR ATTORNY</h2>
  <div class="abs cta-btn">MEET OUR ATTORNY</div>
</section>

<section>
  <h2 class="abs section-title contact-title">CONTCAT US</h2>
  <p class="abs contact-sub">Need An Have Question Please Contact Us Today.</p>
  <div class="abs field" style="left:218px;top:2272px;width:310px;height:45px">Name *</div>
  <div class="abs field" style="left:218px;top:2325px;width:310px;height:45px">Phone *</div>
  <div class="abs field" style="left:218px;top:2380px;width:310px;height:45px">Email *</div>
  <div class="abs field" style="left:537px;top:2272px;width:425px;height:153px">Message *</div>
  <div class="abs btn submit-btn">SUBMIT</div>
</section>

<nav class="abs foot-nav"><span>Home</span><span>About Us</span><span>Practice Area</span><span>Contact Us</span></nav>

<footer>
  <div class="abs site-footer"></div>
  <div class="abs foot-brand">
    <div class="brand-mark"></div>
    <div class="brand-name">CORVANE<br>LEGAL</div>
    <p class="copy">©<b>CORVANE LEGAL</b> - 2018 All<br>Right Reserved.</p>
  </div>

  <h3 class="abs foot-head" style="left:350px">PRACTICE AREAS</h3>
  <ul class="abs foot-list">
    <li>Corporate Transactions &amp; Regulation</li>
    <li>Business Law And Dispute Resolution</li>
    <li>Migration Assistance</li>
  </ul>

  <h3 class="abs foot-head" style="left:615px">CONTACT US</h3>
  <div class="abs foot-contact">
    <div><svg width="18" height="24" viewBox="0 0 18 24"><path d="M9 0C4 0 0 4 0 9c0 6 9 15 9 15s9-9 9-15c0-5-4-9-9-9z" fill="#2e4f8c"/><circle cx="9" cy="9" r="3.5" fill="#0b0b0d"/></svg><span>101 - Lorem is the simple text print and type text.</span></div>
    <div><svg width="18" height="18" viewBox="0 0 24 24"><path d="M6.6 10.8a15 15 0 006.6 6.6l2.2-2.2c.3-.3.7-.4 1-.2 1.1.4 2.3.6 3.6.6.6 0 1 .4 1 1V20c0 .6-.4 1-1 1A17 17 0 013 4c0-.6.4-1 1-1h3.5c.6 0 1 .4 1 1 0 1.2.2 2.4.6 3.6.1.3 0 .7-.2 1z" fill="#2e4f8c"/></svg><span>123 456 7890</span></div>
    <div><svg width="18" height="14" viewBox="0 0 18 14"><rect width="18" height="14" rx="1" fill="#2e4f8c"/><path d="M1 1l8 6 8-6" fill="none" stroke="#0b0b0d" stroke-width="1.5"/></svg><span>info@corvanelegal.com</span></div>
  </div>

  <h3 class="abs foot-head" style="left:897px">FOLLOW US</h3>
  <div class="abs social"></div>
</footer>

</body>
</html>
```